Management Company for Associations needs new and improved letterhead

We need a design for letterhead that looks professional. We like designs that can incorporate a lot of space for our letters, a new age professional font, and different styles to choose from. Please use the language in the attached letterhead example. The BPN logo needs to be incorporated in the letterhead; please follow the size requirements for use. We are trying to totally revamp our letterhead.
Industry/Entity Type
Property Management
Font styles to use
Serif
Script
Colors
ec1f27
Requirements
Must have
- BPN Logo in black, K7 logo, Using both Top & Bottom, Red Color used to match logo color.
Nice to have
- (1 design with a watermark using K7 logo)

```html
<!DOCTYPE html>
<html lang="en">
<head>
<meta charset="utf-8">
<title>K7 Community Partners Letterhead</title>
<link rel="stylesheet" href="https://fonts.googleapis.com/css2?family=Arimo:wght@400;700&display=swap">
<style>
  :root {
    --brand-red: #ec1f27;
    --ink: #1c1c1c;
    --band-dark: #262626;
    --paper: #f2f2f2;
    --backdrop: #d0d0d0;
  }
  * { margin: 0; padding: 0; box-sizing: border-box; }
  html, body { width: 1200px; height: 1041px; overflow: hidden; background: var(--backdrop); }
  body { font-family: "Arimo", Arial, sans-serif; color: var(--ink); }

  .letterhead {
    position: absolute; left: 197px; top: 0;
    width: 806px; height: 1041px;
    background: var(--paper); overflow: hidden;
  }

  .brand { position: absolute; left: 64px; top: 62px; display: flex; align-items: center; }
  .brand-mark { width: 52px; height: 52px; background: var(--brand-red); margin-right: 14px; }
  .brand-name { font-size: 22px; font-weight: 700; color: var(--ink); line-height: 1; letter-spacing: 0.5px; }
  .brand-tagline { font-size: 10px; margin-top: 6px; color: #555; }

  .contact { position: absolute; right: 64px; top: 66px; text-align: right; font-size: 10.5px; line-height: 14px; font-style: normal; }
  .contact-label { color: var(--brand-red); font-weight: 700; }
  .contact-web strong { color: var(--brand-red); font-weight: 700; }

  .letter { position: absolute; left: 64px; width: 677px; font-size: 11px; line-height: 13.7px; }
  .letter-date { top: 272px; }
  .letter-recipient { top: 299px; }
  .letter-body { top: 419px; letter-spacing: -0.15px; }
  .letter-body p { text-align: justify; margin-bottom: 13.7px; }

  .closing { position: absolute; left: 64px; top: 719px; font-size: 11px; line-height: 13.7px; }
  .signature { position: absolute; left: 152px; top: 700px; width: 158px; height: 78px; border-radius: 40px; background: linear-gradient(90deg, rgba(141,164,216,0.15), rgba(141,164,216,0.35), rgba(141,164,216,0.15)); }

  .membership { position: absolute; left: 64px; top: 945px; width: 130px; height: 54px; }
  .membership-badge { width: 130px; height: 54px; border-radius: 4px; background: #cfcfcf; }

  .footer-rule { position: absolute; left: 0; bottom: 22px; width: 806px; height: 3px; background: var(--brand-red); }
  .footer-band { position: absolute; left: 0; bottom: 0; width: 806px; height: 18px; background: var(--band-dark); }
</style>
</head>
<body>
<main class="letterhead">
  <header>
    <div class="brand">
      <div class="brand-mark"></div>
      <div>
        <div class="brand-name">K7 Community Partners</div>
        <div class="brand-tagline">Association management for residential communities since 2004</div>
      </div>
    </div>
    <address class="contact">
      <div><span class="contact-label">Toll Free:</span> 1.800.555.0142</div>
      <div><span class="contact-label">Tel:</span> 555.210.0100</div>
      <div><span class="contact-label">Fax:</span> 555.210.0101</div>
      <div class="contact-web">www.<strong>k7communitypartners</strong>.com</div>
    </address>
  </header>

  <div class="letter letter-date">30.09.2016</div>
  <div class="letter letter-recipient">
    Recipient’s name<br>Musterstraße 12<br>10999 Berlin<br>Germany
  </div>

  <section class="letter letter-body">
    <p>Dear sir,</p>
    <p>Communication is a very integral part of living creatures, animals and humans. Communication may be verbal or written. Written communication however is only applicable to human beings. Can you even imagine a world without communication? Verbal communication can be through telephones, webcams or in person. Written communication is through letters, emails and mobile phone messages.</p>
    <p>In today’s world of great inventions and technology, letters have somehow become redundant. It is the time for text messages or chats. But they still can communicate a lot more than all other modes of communication. Organizations and various government departments still bank on letters as a strong medium of communication. There is no comparison in costs of sending letters as compared to costs of mobile phone messages though – letters are far cheaper. Letters now commonly known as “hard copy documents” are considered more relevant and important than email copies of text messages as proof or evidence of some sort.</p>
    <p>Letters speak volumes about a person or an organization that writes it. So one must take utmost care ensuring that the language used in any letter is appropriate for the occasion for which it is being written. Since a letter is also a written proof or document, if there are certain things that should not form a part of it, then that too should be carefully handled.</p>
    <p>Writing a good letter is an art. But if for some reason someone is unable to write that perfect letter, these different types of letters provide a base for you to build on. Sample letters have been given for everyone to understand what all information needs to form a part of the letter type and then it can be customized.</p>
  </section>

  <div class="closing">Yours Sincerely,<br>Lena Harwood</div>
  <div class="signature" role="img" aria-label="Handwritten signature of Lena Harwood in blue ink"></div>

  <div class="membership">
    <div class="membership-badge" role="img" aria-label="BPN membership badge"></div>
  </div>

  <div class="footer-rule"></div>
  <div class="footer-band"></div>
</main>
</body>
</html>
```